I need creative and unique business card design using my company logo. Ok to change logo color. We are a small brokerage doing both Real Estate and Mortgage services. Need to have the follow on business card;
1. agent name - Mila Fenton - Realtor
2. cell - 949-555-0182
3. license number - DRE 04917362
4. business name - Brightway Estates & Lending, Inc
5. business office - 626-555-0147
6. business address - 287 W. Larkmoor Ave #214, Arcadia CA 91088
7. business logo - attached (ok to use different color on logo)

```html
<!DOCTYPE html>
<html lang="en">
<head>
<meta charset="utf-8">
<title>Brightway Estates &amp; Lending — Business Card</title>
<link rel="stylesheet" href="https://fonts.googleapis.com/css2?family=Montserrat:wght@400;500;700&display=swap">
<style>
  :root {
    --page-bg: #e7e3dd;
    --card-top: #f3f5f7;
    --card-bottom: #e4e9ee;
    --brand-blue: #1f4f96;
    --navy: #173a78;
    --ink: #3a3f47;
    --gold: #c9a574;
    --lic-ink: #c9ced8;
  }
  * { box-sizing: border-box; margin: 0; padding: 0; }
  html, body { width: 1200px; height: 897px; overflow: hidden; }
  body {
    background: var(--page-bg);
    font-family: "Montserrat", sans-serif;
    position: relative;
  }
  .card {
    position: absolute;
    left: 50px; top: 148px;
    width: 1100px; height: 601px;
    border-radius: 24px;
    overflow: hidden;
    background: linear-gradient(160deg, var(--card-top), var(--card-bottom));
    box-shadow: 0 10px 30px rgba(40, 40, 50, 0.18);
  }
  .wave { position: absolute; left: 0; top: 0; width: 1100px; height: 601px; }

  .brand-mark {
    position: absolute;
    left: 257px; top: 174px;
    width: 167px; height: 158px;
    background: var(--brand-blue);
  }
  .brand-name {
    position: absolute;
    left: 150px; width: 380px;
    text-align: center;
    color: var(--brand-blue);
    font-weight: 500;
    text-transform: uppercase;
  }
  .brand-name .primary {
    display: block;
    position: absolute; left: 0; right: 0; top: 360px;
  }
  .brand-primary {
    top: 364px;
    font-size: 31px;
    letter-spacing: 10px;
  }
  .brand-secondary {
    top: 404px;
    font-size: 15px;
    letter-spacing: 3.6px;
  }

  .divider {
    position: absolute;
    left: 554px; top: 170px;
    width: 2px; height: 258px;
    background: var(--brand-blue);
  }

  .agent { position: absolute; left: 606px; top: 164px; color: var(--ink); }
  .agent-name {
    font-size: 39px; font-weight: 700;
    color: var(--navy);
    line-height: 44px;
    letter-spacing: 0.5px;
  }
  .agent-title { font-size: 23px; line-height: 30px; margin-top: 0; }
  .address { font-size: 23px; line-height: 31px; margin-top: 15px; font-style: normal; }
  .contacts { list-style: none; margin-top: 17px; font-size: 24px; line-height: 35px; }
  .contacts li { display: flex; align-items: center; }
  .contacts svg { width: 19px; height: 19px; margin-right: 13px; fill: var(--navy); }

  .license {
    position: absolute;
    right: 58px; top: 555px;
    font-size: 22px;
    color: var(--lic-ink);
    letter-spacing: 0.5px;
  }
</style>
</head>
<body>
  <section class="card">
    <svg class="wave" viewBox="0 0 1100 601" aria-hidden="true">
      <defs>
        <linearGradient id="band" x1="0" y1="0" x2="1" y2="0">
          <stop offset="0" stop-color="#1d4b90"/>
          <stop offset="0.5" stop-color="#2a5aa0"/>
          <stop offset="1" stop-color="#153d80"/>
        </linearGradient>
      </defs>
      <path d="M0 492 C150 560 320 585 540 568 C760 550 900 500 1010 500 C1065 500 1100 525 1100 545 L1100 601 L0 601 Z" fill="url(#band)"/>
      <path d="M0 485 C150 556 320 580 540 563 C760 545 900 508 1000 510 C1055 511 1090 530 1100 545" fill="none" stroke="var(--gold)" stroke-width="2.5"/>
    </svg>

    <div class="brand-mark"></div>
    <div class="brand-name brand-primary">Brightway</div>
    <div class="brand-name brand-secondary">Estates &amp; Lending, Inc</div>

    <div class="divider"></div>

    <div class="agent">
      <h1 class="agent-name">MILA FENTON</h1>
      <p class="agent-title">Realtor</p>
      <address class="address">287 W. Larkmoor Ave #214<br>Arcadia CA 91088</address>
      <ul class="contacts">
        <li>
          <svg viewBox="0 0 20 20" aria-label="Office phone"><path d="M2 8 C2 4 18 4 18 8 L18 10 L14 10 L14 8 C12 7 8 7 6 8 L6 10 L2 10 Z M5 11 L15 11 L17 17 L3 17 Z"/></svg>
          626-555-0147
        </li>
        <li>
          <svg viewBox="0 0 20 20" aria-label="Cell phone"><path d="M6 1 H14 A1.5 1.5 0 0 1 15.5 2.5 V17.5 A1.5 1.5 0 0 1 14 19 H6 A1.5 1.5 0 0 1 4.5 17.5 V2.5 A1.5 1.5 0 0 1 6 1 Z M6.5 3.5 V15 H13.5 V3.5 Z M9 16 H11 V17.5 H9 Z"/></svg>
          949-555-0182
        </li>
        <li>
          <svg viewBox="0 0 20 20" aria-label="Email"><path d="M1 8 L10 2 L19 8 V18 H1 Z M3 9 L10 14 L17 9 L10 4.5 Z"/></svg>
          Mila.fenton@larkpost.com
        </li>
      </ul>
    </div>

    <p class="license">Lic No - DRE 04917362</p>
  </section>
</body>
</html>
```